Lanterns Album Cover

3 panel design, 360mm x 120mm with title 'lanterns' (and sub-title mara tollen) on the right hand panel. Simple clean elegant design with a many stranded ribbon stretching right across the 3 panels, representing 'the river of life' (from the Bible). Plain, muted or textured background color.

```html
<!DOCTYPE html>
<html lang="en">
<head>
<meta charset="UTF-8">
<title>Lanterns – Mara Tollen – Three Panel Cover</title>
<link rel="stylesheet" href="https://fonts.googleapis.com/css2?family=Cinzel:wght@500&family=Oswald:wght@300;500&display=swap">
<style>
  :root {
    --stage: #5b5b5b;
    --sky-light: #f6f5ee;
    --sky-mist: #d8dcd6;
    --sky-grey: #aab3b1;
    --forest-pale: #b9c5ae;
    --forest: #62805a;
    --forest-deep: #3d5841;
    --water: #4f6c8e;
    --water-deep: #2f4566;
    --title-ink: #2c2a35;
    --light-ink: #ffffff;
    --ribbon-gold: #f1e3b8;
    --ribbon-pale: #ffffff;
    --tray-line: rgba(255, 255, 255, 0.55);
  }

  html, body {
    margin: 0;
    padding: 0;
    width: 1200px;
    height: 1200px;
    overflow: hidden;
    background: var(--stage);
  }

  .spread {
    position: absolute;
    left: 30px;
    top: 410px;
    width: 1140px;
    height: 380px;
    display: flex;
  }

  .panel {
    position: relative;
    width: 380px;
    height: 380px;
    overflow: hidden;
  }

  .panel-artwork {
    position: absolute;
    inset: 0;
    background:
      radial-gradient(ellipse 60% 42% at 50% 10%, var(--sky-light) 0%, rgba(246,245,238,0.6) 45%, rgba(246,245,238,0) 100%),
      linear-gradient(180deg,
        var(--sky-mist) 0%,
        var(--sky-light) 22%,
        var(--sky-mist) 44%,
        var(--forest-pale) 56%,
        var(--forest) 67%,
        var(--forest-deep) 77%,
        var(--water) 88%,
        var(--water-deep) 100%);
  }

  .panel-artwork::after {
    content: "";
    position: absolute;
    inset: 0;
    background: linear-gradient(90deg, rgba(170,179,177,0.45) 0%, rgba(170,179,177,0) 20%, rgba(170,179,177,0) 80%, rgba(170,179,177,0.45) 100%);
  }

  /* Left panel: repeated outlined artist name */
  .name-rows {
    position: absolute;
    left: -22px;
    top: -28px;
    margin: 0;
    padding: 0;
    list-style: none;
    font-family: "Oswald", sans-serif;
    font-weight: 500;
    font-size: 78px;
    line-height: 88px;
    letter-spacing: 1px;
    white-space: nowrap;
    color: transparent;
    -webkit-text-stroke: 1.5px rgba(255, 255, 255, 0.75);
    transform: skewX(-10deg);
  }

  .name-rows li:nth-child(n+4) {
    -webkit-text-stroke-color: var(--light-ink);
  }

  /* Middle panel: disc tray */
  .disc-tray {
    position: absolute;
    left: 42px;
    top: 8px;
    width: 296px;
    height: 296px;
    border-radius: 50%;
    border: 1.5px solid var(--tray-line);
    box-shadow: inset 0 0 20px rgba(255, 255, 255, 0.25);
  }

  .panel-frame {
    position: absolute;
    inset: 6px;
    border: 1px solid rgba(255, 255, 255, 0.5);
  }

  .cover-title {
    position: absolute;
    left: 0;
    right: 0;
    margin: 0;
    text-align: center;
    font-family: "Cinzel", serif;
    font-weight: 500;
    line-height: 1;
    color: var(--title-ink);
    text-shadow: 0 0 10px rgba(255, 244, 210, 0.6);
  }

  .cover-artist {
    position: absolute;
    margin: 0;
    font-family: "Oswald", sans-serif;
    font-weight: 300;
    line-height: 1;
    color: var(--light-ink);
    text-shadow: 0 1px 4px rgba(0, 0, 0, 0.35);
  }

  .panel-tray .cover-title { top: 150px; font-size: 60px; letter-spacing: -2px; }
  .panel-tray .cover-artist { right: 18px; top: 222px; font-size: 26px; }

  .panel-front .cover-title { top: 165px; font-size: 52px; letter-spacing: -1px; }
  .panel-front .cover-artist { right: 30px; top: 226px; font-size: 23px; }

  /* River of life ribbon across all three panels */
  .river-ribbon {
    position: absolute;
    left: 0;
    top: 0;
    width: 1140px;
    height: 380px;
    pointer-events: none;
  }

  .river-ribbon path {
    fill: none;
    stroke-linecap: round;
  }
</style>
</head>
<body>
  <main class="spread">
    <section class="panel panel-back">
      <div class="panel-artwork" role="img" aria-label="Photographic scene: misty light behind a tall cross and two doves above a pine forest and reflective lake"></div>
      <ul class="name-rows" aria-label="Mara Tollen">
        <li>MARA TOLLEN</li>
        <li>MARA TOLLEN</li>
        <li>MARA TOLLEN</li>
        <li>MARA TOLLEN</li>
        <li>MARA TOLLEN</li>
      </ul>
    </section>

    <section class="panel panel-tray">
      <div class="panel-artwork" role="img" aria-label="Photographic scene: bright sky with a cross and two white doves over a pine forest and still lake"></div>
      <div class="disc-tray"></div>
      <div class="panel-frame"></div>
      <h2 class="cover-title">LANTERNS</h2>
      <p class="cover-artist">MARA TOLLEN</p>
    </section>

    <section class="panel panel-front">
      <div class="panel-artwork" role="img" aria-label="Photographic scene: rays of light behind a cross and two doves, pine forest with waterfalls on each side flowing into a reflective lake"></div>
      <h1 class="cover-title">LANTERNS</h1>
      <p class="cover-artist">MARA TOLLEN</p>
    </section>

    <svg class="river-ribbon" viewBox="0 0 1140 380" aria-hidden="true">
      <g stroke="var(--ribbon-gold)" opacity="0.55">
        <path d="M0 300 C 190 250, 330 340, 570 295 S 950 255, 1140 300" stroke-width="1.6"/>
        <path d="M0 306 C 190 258, 330 348, 570 302 S 950 262, 1140 307" stroke-width="1.2"/>
        <path d="M0 312 C 190 266, 330 356, 570 309 S 950 269, 1140 314" stroke-width="1.6"/>
        <path d="M0 318 C 190 274, 330 364, 570 316 S 950 276, 1140 321" stroke-width="1"/>
      </g>
      <g stroke="var(--ribbon-pale)" opacity="0.5">
        <path d="M0 303 C 190 254, 330 344, 570 298 S 950 258, 1140 303" stroke-width="0.8"/>
        <path d="M0 309 C 190 262, 330 352, 570 305 S 950 265, 1140 310" stroke-width="0.8"/>
        <path d="M0 315 C 190 270, 330 360, 570 312 S 950 272, 1140 317" stroke-width="0.8"/>
      </g>
    </svg>
  </main>
</body>
</html>
```